Bright Harbor Concierge

I need a website developed for our travel concierge service. I'm looking to be able to collect information and have the information collected directed to a inbox. I would also like to me able to manage the updates to the website myself. I also would like a mobile version of the website to be included. Our services include assistance with Bachelor Parties, Bachelorette Parties and Medical Tourism. We provide custom packages that include Airport Transportation, Lodging, Bilingual guides and any other special needs identified by our clients.
Industry/Entity Type
Travel
Coding
Coded - Design and coding required
Number of Pages Required
4 page
Look and feel

```html
<!DOCTYPE html>
<html lang="en">
<head>
<meta charset="utf-8">
<title>Bright Harbor Concierge</title>
<link href="https://fonts.googleapis.com/css2?family=Marcellus&family=Poppins:wght@300;400;500&display=swap" rel="stylesheet">
<style>
:root{
  --gold:#dc9a2a;
  --gold-soft:#c28a2a;
  --ink:#111111;
  --panel:#1a1a1a;
  --card:#141414;
  --text:#e8e8e8;
  --muted:#a9a9a9;
  --backdrop:#f2f2f2;
}
*{margin:0;padding:0;box-sizing:border-box}
html,body{width:1200px;height:3748px;overflow:hidden;background:var(--backdrop)}
body{font-family:"Poppins",sans-serif;color:var(--text);position:relative}
.page{position:absolute;left:82px;top:60px;width:1044px;height:3628px;background:var(--ink);overflow:hidden}
.abs{position:absolute}
.serif{font-family:"Marcellus",serif;font-weight:400}
.gold{color:var(--gold)}
.btn{position:absolute;background:var(--gold);color:#fff;font-size:11px;display:flex;align-items:center;justify-content:center;border-radius:2px}
.photo{position:absolute}
.hero{position:absolute;left:0;top:0;width:1044px;height:582px;background:linear-gradient(160deg,#3b3b36 0%,#2a2c28 40%,#1e211f 70%,#2b2a24 100%)}
.brand{position:absolute;left:79px;top:28px;display:flex;align-items:center;gap:8px;font-family:"Marcellus",serif;color:var(--gold);font-size:19px}
.brand .dot{width:12px;height:12px;border:1px solid var(--gold);border-radius:50%}
.nav{position:absolute;left:441px;top:41px;display:flex;gap:19px;font-size:11px;color:#ddd}
.nav .active{color:var(--gold)}
.hero h1{position:absolute;left:79px;top:236px;font-size:31px;line-height:43px;color:#f3f3f3}
.hero p{position:absolute;left:79px;top:328px;font-size:10.5px;line-height:19px;color:#ddd}
.about-panel{position:absolute;left:0;top:637px;width:1044px;height:476px;background:var(--panel)}
.about-text{position:absolute;left:470px}
.stat{position:absolute;top:929px}
.stat .rule{width:22px;height:1px;background:var(--gold)}
.stat .lbl{margin-top:19px;font-size:10px;letter-spacing:.8px;color:#ccc}
.stat .num{margin-top:18px;font-family:"Marcellus",serif;font-size:46px;color:var(--gold);line-height:1}
.services-bg{position:absolute;left:0;top:1167px;width:1044px;height:1167px;background:var(--panel)}
.label{font-size:13px;color:var(--gold)}
.card{position:absolute;top:1283px;width:292px;height:412px;background:var(--card);padding:20px}
.card .photo{position:relative;width:252px;height:190px;border:1px solid var(--gold-soft)}
.card h3{margin-top:22px;font-size:15px;color:var(--gold)}
.card p{margin-top:14px;font-size:11.5px;line-height:22px;color:#cfcfcf}
.card svg{position:absolute;right:20px;bottom:22px}
.testi{position:absolute;left:79px;top:2452px;width:883px;height:326px;background:var(--panel)}
.info{position:absolute;left:79px;display:flex;align-items:center;gap:10px;font-size:11px;color:#ddd}
.footer{position:absolute;left:0;top:3407px;width:1044px;height:221px;background:var(--panel)}
.fnav{position:absolute;left:0;width:1044px;top:145px;display:flex;justify-content:center;gap:42px;font-size:11px;color:#ddd}
</style>
</head>
<body>
<main class="page">

  <section class="hero">
    <div class="photo" role="img" aria-label="Person sitting at the end of a wooden pier on a still mountain lake" style="inset:0;background:linear-gradient(180deg,rgba(40,42,40,.6),rgba(20,22,20,.75)),linear-gradient(120deg,#4a4d46,#2c302b 55%,#3a3c33)"></div>
    <div class="brand"><span class="dot"></span>Bright Harbor</div>
    <nav class="nav"><span class="active">Home</span><span>About Us</span><span>Services</span><span>Package</span><span>Why Us</span><span>Contact</span><span>Blog</span></nav>
    <div class="btn" style="left:848px;top:32px;width:114px;height:34px">Let's Talk</div>
    <h1 class="serif">Save your time by using Bright Harbor<br>and present yours.</h1>
    <p>Our service will help you plunge into the world of bachelor, harmony and transquility!<br>A place for tourism, physical development and parties</p>
    <div class="btn" style="left:79px;top:396px;width:113px;height:32px">View our Service</div>
  </section>

  <section>
    <div class="about-panel"></div>
    <div class="photo" role="img" aria-label="Traveller with open arms beneath a tall waterfall" style="left:79px;top:602px;width:337px;height:546px;background:linear-gradient(180deg,#3a3f42,#6a7378 45%,#2c3133 80%,#1c1f1e)"></div>
    <div class="about-text label" style="top:709px">About Us</div>
    <h2 class="about-text serif" style="top:741px;font-size:26px;line-height:37px;color:#f0f0f0">Save your time by using Bright Harbor and<br>present yours.</h2>
    <p class="about-text" style="top:835px;font-size:11px;line-height:22px;color:#ddd">Our service will help you plunge into the world of bachelor, harmony and transquility!<br>A place for tourism, physical development and parties. <span class="gold" style="text-decoration:underline">View More</span></p>
    <div class="stat" style="left:470px"><div class="rule"></div><div class="lbl">AWARDS</div><div class="num">800+</div></div>
    <div class="stat" style="left:644px"><div class="rule"></div><div class="lbl">HAPPY CLIENT</div><div class="num">1200+</div></div>
    <div class="stat" style="left:835px"><div class="rule"></div><div class="lbl">YEARS OF EXPERIENCE</div><div class="num">15+</div></div>
  </section>

  <section class="services-bg"></section>
  <div class="abs label" style="left:79px;top:1233px">Services</div>
  <div class="abs" style="left:148px;top:1243px;width:814px;height:1px;background:var(--gold-soft);opacity:.7"></div>

  <article class="card" style="left:79px">
    <div class="photo" role="img" aria-label="Group of friends raising drinks under palm trees" style="background:linear-gradient(135deg,#c9c6a4,#7f8a5a 50%,#5c5340)"></div>
    <h3 class="serif">Bachelor Parties</h3>
    <p>Our service will help you plunge into the world of bachelor, harmony and transquility!<br>A place for tourism, physical development and parties.</p>
    <svg width="18" height="10" viewBox="0 0 18 10"><path d="M0 5h16M12 1l4 4-4 4" stroke="#dc9a2a" fill="none" stroke-width="1.2"/></svg>
  </article>
  <article class="card" style="left:375px">
    <div class="photo" role="img" aria-label="Surgical team leaning over an operating table" style="background:linear-gradient(135deg,#9fb9a8,#6f8f86 50%,#4b5c5e)"></div>
    <h3 class="serif">Medical Tourism</h3>
    <p>Our service will help you plunge into the world of bachelor, harmony and transquility!<br>A place for tourism, physical development and parties.</p>
    <svg width="18" height="10" viewBox="0 0 18 10"><path d="M0 5h16M12 1l4 4-4 4" stroke="#dc9a2a" fill="none" stroke-width="1.2"/></svg>
  </article>
  <article class="card" style="left:670px">
    <div class="photo" role="img" aria-label="Friends toasting with glasses of wine" style="background:linear-gradient(135deg,#6b3f1f,#3b2416 55%,#2a2a2f)"></div>
    <h3 class="serif">Bachelorette Parties</h3>
    <p>Our service will help you plunge into the world of bachelor, harmony and transquility!<br>A place for tourism, physical development and parties.</p>
    <svg width="18" height="10" viewBox="0 0 18 10"><path d="M0 5h16M12 1l4 4-4 4" stroke="#dc9a2a" fill="none" stroke-width="1.2"/></svg>
  </article>

  <div class="abs label" style="left:79px;top:1877px">Airport Transportation</div>
  <h2 class="abs serif" style="left:79px;top:1917px;font-size:26px;line-height:34px;color:#f0f0f0">We are concern with<br>servicing</h2>
  <div class="abs" style="left:79px;top:2000px;width:440px;font-size:11px;line-height:22px;color:#ddd">
    <p>when an unknown printer took a galley of type and scrambled it to make a type specimen book. It has survived not only five centuries, but also the leap into electronic typesetting, remaining essentially</p>
    <p style="margin-top:9px">It was popularised in the 1960s with the release of Presstype sheets containing Lorem Ipsum passages, and more recently with desktop publishing software like Folio Layout Studio including versions of Lorem</p>
  </div>
  <div class="btn" style="left:79px;top:2178px;width:113px;height:31px">View our Package</div>
  <div class="photo" role="img" aria-label="Passenger jet parked on an airport apron beside shuttle buses" style="left:575px;top:1806px;width:387px;height:439px;border:1px solid var(--gold-soft);background:linear-gradient(180deg,#d8dbdf 0%,#c4c8cc 38%,#8f9590 45%,#a7a8a5 60%,#9c9c98 100%)"></div>
  <svg class="abs" style="left:662px;top:2264px" width="212" height="24" viewBox="0 0 212 24">
    <circle cx="12" cy="12" r="10.5" fill="none" stroke="#888"/><path d="M17 12H7M10 9l-3 3 3 3" stroke="#aaa" fill="none"/>
    <g fill="#777"><circle cx="66" cy="12" r="3"/><circle cx="84" cy="12" r="3"/><circle cx="102" cy="12" r="3"/><circle cx="120" cy="12" r="3"/><circle cx="138" cy="12" r="3"/></g>
    <circle cx="156" cy="12" r="3.5" fill="#dc9a2a"/>
    <circle cx="199" cy="12" r="10.5" fill="none" stroke="#dc9a2a"/><path d="M194 12h10M201 9l3 3-3 3" stroke="#dc9a2a" fill="none"/>
  </svg>

  <h2 class="abs serif gold" style="left:79px;top:2391px;font-size:26px">Testimonials</h2>
  <section class="testi">
    <div class="photo" role="img" aria-label="Portrait of a smiling client" style="left:134px;top:52px;width:132px;height:132px;border-radius:50%;background:radial-gradient(circle at 40% 40%,#8a5a4c,#3a2420 70%)"></div>
    <svg class="abs" style="left:317px;top:52px" width="44" height="36" viewBox="0 0 44 36"><path d="M2 16Q2 3 16 2v7q-6 1-6 7h6v18H2zM26 16q0-13 14-14v7q-6 1-6 7h6v18H26z" fill="#dc9a2a"/></svg>
    <p class="abs" style="left:317px;top:100px;width:440px;font-size:11.5px;line-height:22px;color:#ddd">It was popularised in the 1960s with the release of Presstype sheets containing Lorem Ipsum passages, and more recently with desktop publishing software like Folio Layout Studio including versions of Lorem Ipsum.</p>
    <div class="abs gold" style="left:317px;top:200px;font-size:11px">Marina Holt</div>
    <div class="abs" style="left:317px;top:216px;font-size:7.5px;color:#999">Co-founder, Lorem</div>
    <div class="abs gold" style="left:317px;top:245px;font-size:9px;display:flex;align-items:center;gap:5px">01<span style="width:50px;height:1px;background:var(--gold)"></span>08</div>
    <svg class="abs" style="left:674px;top:240px" width="76" height="24" viewBox="0 0 76 24">
      <circle cx="12" cy="12" r="10.5" fill="none" stroke="#777"/><path d="M17 12H7M10 9l-3 3 3 3" stroke="#999" fill="none"/>
      <circle cx="63" cy="12" r="10.5" fill="none" stroke="#dc9a2a"/><path d="M58 12h10M65 9l3 3-3 3" stroke="#dc9a2a" fill="none"/>
    </svg>
  </section>

  <h2 class="abs serif gold" style="left:79px;top:2891px;font-size:26px">Contact Us</h2>
  <div class="abs" style="left:79px;top:3013px;width:418px;height:56px;display:flex">
    <div style="flex:0 0 267px;background:#fff;color:#888;font-size:12px;display:flex;align-items:center;padding-left:15px">Enter Your Phone</div>
    <div style="flex:1;background:var(--gold);color:#fff;font-size:13px;display:flex;align-items:center;justify-content:center">Request</div>
  </div>
  <div class="info" style="top:3139px"><svg width="12" height="14" viewBox="0 0 12 14"><path d="M6 13S1.5 8.5 1.5 5.5a4.5 4.5 0 0 1 9 0C10.5 8.5 6 13 6 13z" fill="none" stroke="#dc9a2a"/><circle cx="6" cy="5.5" r="1.6" fill="none" stroke="#dc9a2a"/></svg>00 Lorem Ipsum, United State of America</div>
  <div class="info" style="top:3170px"><svg width="12" height="12" viewBox="0 0 12 12"><circle cx="6" cy="6" r="5" fill="none" stroke="#dc9a2a"/><circle cx="6" cy="6" r="2" fill="none" stroke="#dc9a2a"/></svg>hello@brightharbor.example</div>
  <div class="info" style="top:3202px"><svg width="12" height="12" viewBox="0 0 12 12"><path d="M2 1h3l1 3-1.5 1a7 7 0 0 0 2.5 2.5L8 6l3 1v3a1 1 0 0 1-1 1A9 9 0 0 1 1 2a1 1 0 0 1 1-1z" fill="none" stroke="#dc9a2a"/></svg>+00 000 00 0000</div>
  <div class="photo" role="img" aria-label="Decorative gold dot pattern" style="left:740px;top:2923px;width:216px;height:196px;background:radial-gradient(circle,rgba(220,154,42,.55) 0,rgba(220,154,42,.15) 70%);opacity:.5"></div>
  <div class="photo" role="img" aria-label="Illuminated iron tower against a night sky" style="left:565px;top:2971px;width:333px;height:381px;border:1px solid var(--gold-soft);background:radial-gradient(ellipse at 55% 65%,#6a4e1c 0%,#1a1420 40%,#08060f 75%)"></div>

  <footer class="footer">
    <div class="abs" style="left:0;width:1044px;top:48px;display:flex;justify-content:center;align-items:center;gap:8px;font-family:'Marcellus',serif;color:var(--gold);font-size:20px"><span style="width:12px;height:12px;border:1px solid var(--gold);border-radius:50%"></span>Bright Harbor</div>
    <nav class="fnav"><span class="gold">Home</span><span>About Us</span><span>Services</span><span>Package</span><span>Why Us</span><span>Contact</span><span>Blog</span></nav>
    <div class="abs" style="left:79px;top:196px;font-size:10px;color:#ddd">© 2021 Bright Harbor. All rights reserved</div>
    <div class="abs" style="right:82px;top:196px;font-size:10px;color:#ddd;display:flex;gap:22px"><span>Teams of Service</span><span>Privacy policy</span></div>
  </footer>
</main>
</body>
</html>
```